Wealth Management Business Card

We are a professional services consulting firm that specializes in high net worth individuals over $25,000,000, executives C-suite and above, closely held businesses owners, family offices and highly compensated employees.

Our focus is on risk mitigation and tax efficient strategies. Our clients take their risk on themselves and have a proven track record generating wealth. Our directive is to preserve and protect the wealth they’ve already created.

Our company Harbridge Advisory is geared around five directives of asset protection:
1) Legal Structuring
2) Leverage & Financing
3) Risk Management - Asset Protection & Insurance, Trustee Work
4) Asset Management & Investing - Under www.qelvantcapital.com
5) Tax Efficient Strategies

Our Company Mark is a Pentagon with a key in the middle. A pentagon is the most efficient defensive structure. Each point of a pentagon is equal distance front every point . Each side provides support to another and works together, which is the key to our clients success.

Our key colors are blue, black and silver.

We ‘re located in the Pacific Northwest with bi coastal and international clients. We have fewer, higher net worth clients and provide exceptional customer service. We do not do social media.

website is www.harbridgepath.com

Target Market(s)

High End Clients

Contact Information for Business Card

extra thick

Font styles to use
Serif

Requirements
Must have
• Metalic foil for lettering.
Black Background on one side
White Background on the other
Horizontal Format Only
No Rounded corners
Not Marketing sales information on the card.
Nice to have
• imprinted texture on the card
Should not have
• lots of color

```html
<!DOCTYPE html>
<html lang="en">
<head>
<meta charset="utf-8">
<title>Harbridge Advisory – Business Card</title>
<link rel="stylesheet" href="https://fonts.googleapis.com/css2?family=Cinzel:wght@400;600&family=Arimo:wght@400&display=swap">
<style>
  :root {
    --canvas: #ffffff;
    --card-black: #0c0c0c;
    --card-black-light: #1a1a1a;
    --card-white: #ffffff;
    --foil-blue: #1f8fff;
    --foil-navy: #14209a;
    --foil-silver: #c9c9c9;
    --ink: #1e1e1e;
    --caption: #111111;
    --card-shadow: 0 2px 5px rgba(0,0,0,0.35);
  }
  * { box-sizing: border-box; margin: 0; padding: 0; }
  html, body {
    width: 1200px; height: 1000px; overflow: hidden;
    background: var(--canvas);
  }
  .sheet { position: relative; width: 1200px; height: 1000px; }

  .card-view { position: absolute; top: 290px; width: 578px; }
  .card-view--front { left: 12px; }
  .card-view--back { left: 611px; }

  .card {
    position: relative; width: 578px; height: 330px;
    box-shadow: var(--card-shadow); overflow: hidden;
  }
  .card--black { background: var(--card-black); }
  .card__texture {
    position: absolute; inset: 0;
    background: linear-gradient(135deg, var(--card-black-light) 0%, var(--card-black) 50%, var(--card-black-light) 100%);
  }
  .card--white { background: var(--card-white); }

  .brand {
    position: absolute; display: flex; flex-direction: column; align-items: center;
    font-family: "Cinzel", serif; font-weight: 600; text-align: center;
  }
  .brand__mark { border-radius: 50%; }
  .brand__name { line-height: 1.05; letter-spacing: 0.04em; }

  .brand--front { left: 0; right: 0; top: 92px; color: var(--foil-silver); }
  .brand--front .brand__mark { width: 66px; height: 66px; background: var(--foil-blue); margin-bottom: 22px; }
  .brand--front .brand__name { font-size: 34px; }

  .brand--back { left: 40px; width: 210px; top: 100px; color: var(--foil-navy); }
  .brand--back .brand__mark { width: 54px; height: 54px; background: var(--foil-navy); margin-bottom: 20px; }
  .brand--back .brand__name { font-size: 26px; }

  .contact {
    position: absolute; left: 290px; top: 66px;
    font-family: "Cinzel", serif; color: var(--ink);
  }
  .contact__name { font-size: 24px; font-weight: 400; color: var(--foil-blue); line-height: 1; }
  .contact__title { font-size: 16px; margin-top: 2px; letter-spacing: 0.02em; }
  .contact__phone { font-size: 19px; margin-top: 40px; }
  .contact__line { font-size: 13px; margin-top: 6px; }
  .contact__address { font-size: 14.5px; margin-top: 20px; line-height: 1.2; }

  .caption {
    margin-top: 22px; text-align: center;
    font-family: "Arimo", sans-serif; font-size: 17px; line-height: 1.3; color: var(--caption);
  }
</style>
</head>
<body>
<main class="sheet">

  <section class="card-view card-view--front">
    <div class="card card--black">
      <div class="card__texture" role="img" aria-label="Subtle embossed diagonal texture on black card stock"></div>
      <div class="brand brand--front">
        <span class="brand__mark"></span>
        <span class="brand__name">Harbridge Advisory</span>
      </div>
    </div>
    <p class="caption">Black Background<br>Blue Foil + Silver Foil + Black Foil</p>
  </section>

  <section class="card-view card-view--back">
    <div class="card card--white">
      <div class="brand brand--back">
        <span class="brand__mark"></span>
        <span class="brand__name">Harbridge<br>Advisory</span>
      </div>
      <div class="contact">
        <p class="contact__name">Place for Name</p>
        <p class="contact__title">Founder</p>
        <p class="contact__phone">(503) 555-0148</p>
        <p class="contact__line">info@harbridgepath.com</p>
        <p class="contact__line">www.harbridgepath.com</p>
        <p class="contact__address">418 Alder Crest Rd, Suite 12,<br>Lakeview, OR 97099</p>
      </div>
    </div>
    <p class="caption">White Background<br>Blue Foil + Black Foil + Spot UV (or varnish) on Logo</p>
  </section>

</main>
</body>
</html>
```